AMAZING FLYERS, POSTCARDS, AND MARKETING!!!! - Northbeam Shingle & Gutter Works, LLC

This project will be for Northbeam Shingle & Gutter Works, LLC. The flyers and postcards will be used to saturate the Alaska market with our services, and get our name and logo out there for people to remember. We plan to send the flyers and postcards out in a broad scale (both door to door and mail out). We want to send out flyers to realty and property management businesses to introduce our roofing company, and to advertise our services. We would also like to have another version, or the ability to edit the text of the final product to send out the same materials to residential clients (homeowners) by just changing the text slightly to better fit that market.
We have a logo, but need something put together that we can tri-fold and mail out to potential clients. We are planning to do some postcards as well. We would like the option to mail them or bring them to people in person.
We are a locally owned roofing and repair company in Alaska. We would like something professional that will capture their attention and show the potential of working with our company. I included some detailed information about our company and some pictures below of our work trailer and a before/after on a recent project. I also attached our logo files. Please go through the attached data and let us know what you come up with to stir up the marketing aspect of our company. Thank you for your time and consideration.
Updates

Project Deadline Extended
Reason: Allowing additional time for designers to submit/resubmit their flyer/postcard ideas based on inquiries and feedback.

Target Market(s)

1.) Homeowners are the first target market.
2.)Realtors and Property Management companies are the second market

Industry/Entity Type

Marketing

Contact Information for Business Card

Include the logo and contact information for our company. These business cards will be for the Owner, Marcus Velloway, II.
There is also a Co-Owner, Trina Velloway, so we will need the ability to print business cards for each owner. Need to be able to change the title/name and phone number for Trina's contact information please. Contact information, license #, and logo information on one side of the card. Please tell the potential client a little about us on the back of the card by utilizing the attached information.

Requirements
Must have
• Pertinent information about our company and listed in the company information attachment. Attention getting details and design work. Professional in appearance and unique to our company to set us above the general advertisers in this industry.
Nice to have
• Something that sets our flyers apart from the ones people get every day. We want to rise above normal with our advertising.
Should not have
• Nothing plain and boring.

```html
<!DOCTYPE html>
<html lang="en">
<head>
<meta charset="utf-8">
<title>Northbeam Shingle &amp; Gutter Works – Postcards</title>
<link rel="stylesheet" href="https://fonts.googleapis.com/css2?family=Open+Sans:wght@400;600;700&display=swap">
<style>
  :root {
    --brand-blue: #1aa3e0;
    --brand-blue-deep: #0a78b8;
    --ink: #1c1c1c;
    --paper: #ffffff;
    --grey-text: #6d6d6d;
    --stage: #e4e4e4;
    --line: #b9b9b9;
  }
  * { box-sizing: border-box; margin: 0; padding: 0; }
  html, body {
    width: 1038px; height: 1200px; overflow: hidden;
    background: var(--stage);
    font-family: "Open Sans", Arial, sans-serif;
  }
  .canvas { position: relative; width: 1038px; height: 1200px; }

  .card { position: absolute; overflow: hidden; background: var(--paper);
    box-shadow: 0 6px 16px rgba(0,0,0,.25); }
  .card > svg.card-art { position: absolute; inset: 0; }

  .company-name { position: absolute; display: flex; flex-direction: column; justify-content: center;
    text-align: center; font-weight: 700; color: var(--ink); text-transform: uppercase; letter-spacing: .5px; }

  /* ---------- front ---------- */
  .front { left: 86px; top: 45px; width: 690px; height: 530px; }
  .front .company-name { left: 40px; top: 56px; width: 152px; height: 128px; font-size: 16px; line-height: 21px; }
  .front .headline { position: absolute; left: 202px; top: 46px; color: var(--brand-blue);
    font-weight: 600; font-size: 23px; line-height: 26px; text-transform: uppercase; }
  .front .services-title { position: absolute; left: 204px; top: 130px; font-weight: 700;
    font-size: 18px; color: var(--ink); }
  .front .service { position: absolute; font-size: 19px; color: var(--ink);
    display: flex; align-items: center; gap: 6px; }
  .bullet-arrow { width: 13px; height: 13px; border-radius: 50%; background: var(--ink);
    position: relative; flex: none; }
  .bullet-arrow::after { content: ""; position: absolute; left: 4px; top: 3.5px;
    border-left: 5px solid #fff; border-top: 3px solid transparent; border-bottom: 3px solid transparent; }
  .front .pitch { position: absolute; right: 21px; top: 240px; width: 262px; text-align: right;
    font-size: 12px; line-height: 14px; color: var(--grey-text); }
  .front .cta { position: absolute; right: 21px; top: 414px; color: #fff; font-size: 13px; font-weight: 600; }
  .front .phone { position: absolute; right: 21px; top: 445px; color: #fff; font-size: 23px;
    font-weight: 600; display: flex; align-items: center; gap: 8px; }
  .front .email { position: absolute; right: 21px; top: 487px; color: #fff; font-size: 15px; font-weight: 700; }

  /* ---------- back ---------- */
  .back { left: 193px; top: 616px; width: 688px; height: 532px; }
  .back .intro { position: absolute; left: 16px; top: 18px; width: 390px; color: #fff; }
  .back .intro h2 { color: var(--brand-blue); font-size: 11px; font-weight: 700; text-transform: uppercase; }
  .back .intro p { font-size: 9.6px; line-height: 12.2px; text-align: justify; }
  .back .perks { position: absolute; left: 26px; top: 343px; list-style: none; }
  .back .perks li { color: #fff; font-size: 13px; height: 24.5px; display: flex; align-items: center; gap: 9px; }
  .back .perks li::before { content: ""; width: 9px; height: 9px; border-radius: 50%; background: var(--brand-blue); }
  .back .company-name { left: 434px; top: 24px; width: 126px; height: 84px; font-size: 12px; line-height: 16px; }
  .back .stamp { position: absolute; left: 574px; top: 25px; width: 96px; height: 58px; border: 1px solid #9a9a9a; }
  .back .address-line { position: absolute; left: 445px; width: 225px; height: 1px; background: var(--line); }
  .back .phone { position: absolute; left: 205px; top: 494px; color: var(--ink); font-size: 18px;
    display: flex; align-items: center; gap: 8px; }
</style>
</head>
<body>
<main class="canvas">

  <!-- Front of postcard -->
  <section class="card front">
    <svg class="card-art" width="690" height="530" viewBox="0 0 690 530">
      <defs>
        <linearGradient id="paperFade" x1="0" y1="0" x2="1" y2="0">
          <stop offset="0" stop-color="#f7f7f7"/><stop offset="1" stop-color="#e3e3e3"/>
        </linearGradient>
        <linearGradient id="housePhoto" x1="0" y1="0" x2="0" y2="1">
          <stop offset="0" stop-color="#b9c4cc"/><stop offset=".45" stop-color="#8c8f92"/>
          <stop offset=".75" stop-color="#5e6a52"/><stop offset="1" stop-color="#47553a"/>
        </linearGradient>
        <linearGradient id="insetPhoto" x1="0" y1="0" x2="0" y2="1">
          <stop offset="0" stop-color="#7ea46c"/><stop offset=".5" stop-color="#a39c90"/><stop offset="1" stop-color="#6d7a5a"/>
        </linearGradient>
        <linearGradient id="darkPanel" x1="0" y1="0" x2="0" y2="1">
          <stop offset="0" stop-color="#3a3a3a"/><stop offset="1" stop-color="#1b1b1b"/>
        </linearGradient>
        <linearGradient id="blueBand" x1="0" y1="0" x2="1" y2="0">
          <stop offset="0" stop-color="#1aa3e0"/><stop offset="1" stop-color="#0a78b8"/>
        </linearGradient>
      </defs>
      <rect width="690" height="530" fill="url(#paperFade)"/>
      <rect width="690" height="16" fill="#1c1c1c"/>
      <path d="M340 530 C360 430 355 360 420 350 C520 340 600 320 690 290 L690 530 Z" fill="url(#darkPanel)"/>
      <path d="M300 300 C360 350 390 362 430 352 C520 338 610 318 690 286" fill="none" stroke="#1aa3e0" stroke-width="7"/>
      <path d="M338 530 C356 440 350 380 325 335" fill="none" stroke="#d2d2d2" stroke-width="14"/>
      <g role="img" aria-label="Photo of a grey house with a freshly roofed garage and driveway">
        <path d="M0 250 C90 228 200 235 275 280 C330 320 345 420 332 530 L0 530 Z" fill="url(#housePhoto)"/>
      </g>
      <path d="M0 244 C90 222 200 228 282 274" fill="none" stroke="#1aa3e0" stroke-width="6"/>
      <path d="M332 530 C346 420 330 320 275 280" fill="none" stroke="#1aa3e0" stroke-width="5"/>
      <circle cx="272" cy="262" r="54" fill="#fff"/>
      <circle cx="272" cy="262" r="52" fill="none" stroke="#1aa3e0" stroke-width="6"/>
      <g role="img" aria-label="Inset photo of the house roof after repair">
        <circle cx="272" cy="262" r="45" fill="url(#insetPhoto)"/>
      </g>
      <rect x="356" y="442" width="334" height="38" fill="url(#blueBand)"/>
    </svg>

    <div class="company-name"><span>Northbeam</span><span>Shingle &amp;</span><span>Gutter Works</span></div>
    <h1 class="headline">Giving peace of mind to Alaskans,<br>one roof at a time.</h1>
    <div class="services-title">OUR SERVICES:</div>
    <div class="service" style="left:206px;top:158px"><span class="bullet-arrow"></span>Roof repairs</div>
    <div class="service" style="left:206px;top:184px"><span class="bullet-arrow"></span>Commercial roofing</div>
    <div class="service" style="left:454px;top:158px"><span class="bullet-arrow"></span>Roof installations</div>
    <div class="service" style="left:454px;top:184px"><span class="bullet-arrow"></span>Roof inspections</div>
    <p class="pitch">With over two decades of experience in the roofing and repair industry, we would appreciate the opportunity to interview to be your roofing company of choice.</p>
    <div class="cta">CALL US NOW FOR A FREE ESTIMATES</div>
    <div class="phone">
      <svg width="22" height="22" viewBox="0 0 24 24" aria-hidden="true"><circle cx="12" cy="12" r="10.5" fill="none" stroke="#fff" stroke-width="1.8"/><path d="M8.6 6.8l1.8-.4 1.1 2.6-1.2 1a7 7 0 003.7 3.7l1-1.2 2.6 1.1-.4 1.8c-4.6.3-8.9-4-8.6-8.6z" fill="#fff"/></svg>
      907-555-0142
    </div>
    <div class="email">roofs@nsgw907.com</div>
  </section>

  <!-- Back of postcard -->
  <section class="card back">
    <svg class="card-art" width="688" height="532" viewBox="0 0 688 532">
      <defs>
        <linearGradient id="headerBlack" x1="0" y1="0" x2="1" y2="0">
          <stop offset="0" stop-color="#111"/><stop offset="1" stop-color="#333"/>
        </linearGradient>
        <linearGradient id="roofPhoto" x1="0" y1="0" x2="0" y2="1">
          <stop offset="0" stop-color="#a8acae"/><stop offset=".4" stop-color="#6b6f72"/><stop offset="1" stop-color="#4e5256"/>
        </linearGradient>
        <linearGradient id="trailerPhoto" x1="0" y1="0" x2="0" y2="1">
          <stop offset="0" stop-color="#c97a6a"/><stop offset=".18" stop-color="#2a2a2a"/><stop offset="1" stop-color="#111"/>
        </linearGradient>
        <linearGradient id="footBand" x1="0" y1="0" x2="1" y2="0">
          <stop offset="0" stop-color="#1aa3e0"/><stop offset=".5" stop-color="#52bff0"/><stop offset="1" stop-color="#0a78b8"/>
        </linearGradient>
        <linearGradient id="footLight" x1="0" y1="0" x2="0" y2="1">
          <stop offset="0" stop-color="#fafafa"/><stop offset="1" stop-color="#d6d6d6"/>
        </linearGradient>
      </defs>
      <g role="img" aria-label="Photo of new grey asphalt shingles on a roof ridge">
        <rect x="0" y="100" width="425" height="232" fill="url(#roofPhoto)"/>
      </g>
      <path d="M0 0 H405 L428 28 L420 124 L340 110 H0 Z" fill="url(#headerBlack)"/>
      <path d="M405 0 L428 28 L420 124 L400 112 Z" fill="#444"/>
      <path d="M0 319 H418 C428 390 420 440 395 480 H0 Z" fill="#1c1c1c"/>
      <path d="M418 319 C428 390 420 440 395 480" fill="none" stroke="#1aa3e0" stroke-width="6"/>
      <rect x="0" y="478" width="688" height="54" fill="url(#footBand)"/>
      <rect x="0" y="482" width="420" height="42" fill="url(#footLight)"/>
      <g role="img" aria-label="Photo of the company work trailer with ladders on top">
        <rect x="455" y="383" width="218" height="128" fill="url(#trailerPhoto)"/>
      </g>
    </svg>

    <div class="intro">
      <h2>Northbeam Shingle &amp; Gutter Works</h2>
      <p>We've been working in the nearby area and would like to introduce ourselves to your neighborhood. Northbeam Shingle &amp; Gutter Works, LLC is a local business, owned and operated by people born and raised right here in Alaska. We love our state and the sense of community that is uniquely Alaskan, and strive to give you the best service possible.</p>
    </div>

    <ul class="perks">
      <li>Locally owned and operated</li>
      <li>Over two decades in the roofing and repair industry</li>
      <li>Licensed</li>
      <li>Bonded</li>
      <li>Insured</li>
    </ul>

    <div class="company-name"><span>Northbeam</span><span>Shingle &amp;</span><span>Gutter Works</span></div>
    <div class="stamp"></div>
    <div class="address-line" style="top:191px"></div>
    <div class="address-line" style="top:222px"></div>
    <div class="address-line" style="top:253px"></div>
    <div class="address-line" style="top:283px"></div>
    <div class="address-line" style="top:314px"></div>
    <div class="address-line" style="top:345px"></div>

    <div class="phone">
      <svg width="19" height="19" viewBox="0 0 24 24" aria-hidden="true"><circle cx="12" cy="12" r="10.5" fill="none" stroke="#1c1c1c" stroke-width="1.8"/><path d="M8.6 6.8l1.8-.4 1.1 2.6-1.2 1a7 7 0 003.7 3.7l1-1.2 2.6 1.1-.4 1.8c-4.6.3-8.9-4-8.6-8.6z" fill="#1c1c1c"/></svg>
      907-555-0142
    </div>
  </section>

</main>
</body>
</html>
```